Create letterhead in Word or Google Docs

This request is to create an document I can use as an online template for my company letterhead. I don't care much about the design. I just need a letterhead in Word or Google Docs that I can use to draft a letter and send attached to an email. I have a company logo you can attach.

```html
<!DOCTYPE html>
<html lang="en">
<head>
<meta charset="utf-8">
<title>Company Letterhead</title>
<link href="https://fonts.googleapis.com/css2?family=Tinos:wght@400&display=swap" rel="stylesheet">
<style>
  :root {
    --backdrop: #e4e4e4;
    --paper: #ffffff;
    --navy: #252a6e;
    --royal: #2f3a9a;
    --sky: #1f7fc8;
    --ink: #1a1a1a;
    --seal-fill: #a7a3c8;
    --seal-ring: #c9c9d4;
    --seal-text: #c4c2dc;
  }
  * { margin: 0; padding: 0; box-sizing: border-box; }
  html, body {
    width: 1200px;
    height: 1007px;
    overflow: hidden;
    background: var(--backdrop);
    font-family: "Tinos", "Times New Roman", serif;
    color: var(--ink);
  }
  .letterhead {
    position: absolute;
    left: 300px;
    top: 78px;
    width: 600px;
    height: 850px;
    background: var(--paper);
    overflow: hidden;
  }
  .corner-band {
    position: absolute;
    width: 600px;
    height: 850px;
    left: 0;
    top: 0;
  }
  .letterhead-art {
    position: absolute;
    inset: 0;
    width: 600px;
    height: 850px;
  }
  .brand-name {
    position: absolute;
    left: 12px;
    top: 113px;
    width: 154px;
    text-align: center;
    font-size: 30px;
    color: #ffffff;
    line-height: 1;
  }
  .company-block {
    position: absolute;
    left: 231px;
    top: 80px;
  }
  .company-name {
    font-size: 21px;
    line-height: 1;
    margin-bottom: 7px;
  }
  .contact-line {
    font-size: 16px;
    line-height: 23px;
  }
  .salutation {
    position: absolute;
    left: 120px;
    top: 236px;
    font-size: 24px;
    line-height: 1;
  }
  .recipient {
    position: absolute;
    left: 120px;
    top: 283px;
    font-size: 15px;
    line-height: 1;
  }
  .seal-name {
    position: absolute;
    left: 112px;
    top: 448px;
    width: 382px;
    text-align: center;
    font-size: 54px;
    line-height: 1;
    color: var(--seal-text);
  }
  .signature {
    position: absolute;
    left: 428px;
    top: 684px;
    width: 126px;
    border-top: 2px dotted var(--ink);
    padding-top: 6px;
    text-align: center;
    font-size: 22px;
    line-height: 1;
  }
</style>
</head>
<body>
  <main class="letterhead">
    <svg class="corner-band" viewBox="0 0 600 850" role="img" aria-label="Decorative blue wave band across the top right corner">
      <defs>
        <linearGradient id="band-top" x1="0" y1="0" x2="1" y2="0">
          <stop offset="0" stop-color="var(--navy)"/>
          <stop offset="1" stop-color="var(--sky)"/>
        </linearGradient>
      </defs>
      <path d="M10,0 C300,20 540,90 600,190 L600,0 Z" fill="url(#band-top)"/>
    </svg>

    <svg class="corner-band" viewBox="0 0 600 850" role="img" aria-label="Decorative blue wave band across the bottom left corner">
      <defs>
        <linearGradient id="band-bottom" x1="1" y1="0" x2="0" y2="0">
          <stop offset="0" stop-color="var(--navy)"/>
          <stop offset="1" stop-color="var(--sky)"/>
        </linearGradient>
      </defs>
      <path d="M0,690 C40,793 300,833 600,850 L0,850 Z" fill="url(#band-bottom)"/>
    </svg>

    <svg class="letterhead-art" viewBox="0 0 600 850" aria-hidden="true">
      <path d="M140,195 L600,195" stroke="var(--navy)" stroke-width="2"/>
      <path d="M140,200 L600,200" stroke="var(--seal-ring)" stroke-width="1"/>
      <circle cx="89" cy="131" r="84" fill="var(--paper)" stroke="var(--navy)" stroke-width="2"/>
      <circle cx="89" cy="131" r="76" fill="var(--navy)"/>
      <ellipse cx="303" cy="476" rx="191" ry="149" fill="none" stroke="var(--seal-ring)" stroke-width="2"/>
      <ellipse cx="303" cy="476" rx="169" ry="131" fill="var(--seal-fill)"/>
    </svg>

    <div class="brand-name">Halvora</div>

    <header class="company-block">
      <p class="company-name">Compny name</p>
      <p class="contact-line">Phone :</p>
      <p class="contact-line">Email :</p>
      <p class="contact-line">Website :</p>
    </header>

    <p class="salutation">Dear</p>
    <p class="recipient">Mr. XYZ</p>

    <div class="seal-name">Halvora</div>

    <p class="signature">Signature</p>
  </main>
</body>
</html>
```